Vorapo Business Card

Need a double sided business card. Would like the business card to have the logo on one side and the employees details and business contact details on the other.

Business

```html
<!DOCTYPE html>
<html lang="en">
<head>
<meta charset="utf-8">
<title>Vorapo Business Card</title>
<link href="https://fonts.googleapis.com/css2?family=Roboto:wght@300;400;700;900&display=swap" rel="stylesheet">
<style>
  :root {
    --lime: #9dc63f;
    --paper: #f7f7f5;
    --ink: #2b2b2b;
    --muted: #555555;
    --slate: #6b7780;
    --backdrop: #e4e5e6;
  }
  * { margin: 0; padding: 0; box-sizing: border-box; }
  html, body {
    width: 1200px;
    height: 1200px;
    overflow: hidden;
    background: var(--backdrop);
    font-family: "Roboto", "Helvetica Neue", Arial, sans-serif;
  }
  .sheet {
    position: relative;
    width: 1200px;
    height: 1200px;
  }
  .card {
    position: absolute;
    left: 180px;
    width: 840px;
    height: 480px;
    overflow: hidden;
    box-shadow: 0 6px 18px rgba(0,0,0,0.12);
  }
  .card--front {
    top: 100px;
    background: var(--lime);
  }
  .card--back {
    top: 620px;
    background: var(--paper);
    display: flex;
  }
  .wordmark {
    position: absolute;
    right: 70px;
    bottom: 80px;
    display: flex;
    align-items: center;
    gap: 16px;
    color: #ffffff;
    font-weight: 700;
    font-size: 96px;
    letter-spacing: -1px;
    line-height: 1;
  }
  .wordmark__square {
    width: 52px;
    height: 52px;
    background: var(--slate);
  }
  .back__band {
    width: 310px;
    height: 100%;
    background: var(--lime);
  }
  .back__details {
    flex: 1;
    padding: 200px 0 0 50px;
    color: var(--ink);
  }
  .person__name {
    font-size: 44px;
    line-height: 1;
    letter-spacing: 0.5px;
  }
  .person__first { font-weight: 300; }
  .person__last { font-weight: 900; }
  .person__role {
    font-size: 20px;
    font-weight: 300;
    font-style: italic;
    color: var(--muted);
    margin-top: 4px;
  }
  .contact {
    list-style: none;
    margin-top: 18px;
  }
  .contact__item {
    display: flex;
    align-items: center;
    gap: 14px;
    font-size: 24px;
    font-weight: 400;
    color: var(--ink);
    line-height: 1.45;
  }
  .contact__icon {
    width: 20px;
    height: 20px;
    flex: none;
  }
</style>
</head>
<body>
<main class="sheet">
  <section class="card card--front" aria-label="Card front">
    <div class="wordmark">
      <span class="wordmark__name">vorapo</span>
      <span class="wordmark__square"></span>
    </div>
  </section>

  <section class="card card--back" aria-label="Card back">
    <div class="back__band"></div>
    <div class="back__details">
      <h1 class="person__name"><span class="person__first">LENA</span> <span class="person__last">MARSH</span></h1>
      <p class="person__role">Executive Marketing</p>
      <ul class="contact">
        <li class="contact__item">
          <svg class="contact__icon" viewBox="0 0 20 20" aria-hidden="true">
            <rect x="1" y="4" width="18" height="12" rx="1.5" fill="#2b2b2b"/>
            <path d="M2 5 L10 11 L18 5" fill="none" stroke="#f7f7f5" stroke-width="1.6"/>
          </svg>
          lena@vorapo.com
        </li>
        <li class="contact__item">
          <svg class="contact__icon" viewBox="0 0 20 20" aria-hidden="true">
            <rect x="5" y="1" width="10" height="18" rx="2" fill="none" stroke="#2b2b2b" stroke-width="2"/>
            <rect x="8" y="15" width="4" height="1.6" fill="#2b2b2b"/>
          </svg>
          412-530-617
        </li>
        <li class="contact__item">
          <svg class="contact__icon" viewBox="0 0 20 20" aria-hidden="true">
            <rect x="1" y="1" width="18" height="18" rx="3" fill="#2b2b2b"/>
            <rect x="8.8" y="8" width="2.4" height="8" fill="#f7f7f5"/>
            <circle cx="10" cy="5" r="1.5" fill="#f7f7f5"/>
          </svg>
          www.vorapo.com
        </li>
      </ul>
    </div>
  </section>
</main>
</body>
</html>
```